Freelance business trainer needs a new business card

My business is called Tbrite. I provide training in the workplace on management, coaching and mentoring, and customer service topics for a variety of businesses, colleges and private training providers, and teach on management programs. I need a professional but eye catching business card. Business colours grey and orange. My name Linda Marchbank; Tel 07853 416207; email lmarchbank@tbrite.co.uk; website www.tbrite.co.uk.
Happy to have some sort of logo on front and details on back or all on one side
Target Market(s)
SME businesses and colleges - workshops i run are for adults in the workplace
Industry/Entity Type
Training
Look and feel

```html
<!DOCTYPE html>
<html lang="en">
<head>
<meta charset="utf-8">
<title>Tbrite business card</title>
<link rel="stylesheet" href="https://fonts.googleapis.com/css2?family=Cinzel:wght@400;600&family=Open+Sans:wght@400;600&display=swap">
<style>
  :root {
    --page: #e9e6e1;
    --card-white: #ffffff;
    --card-mist: #f0f0f0;
    --ink: #2e2f30;
    --ink-soft: #6a6b6c;
    --orange: #e0521f;
    --orange-deep: #c4441a;
    --slate: #3a3c3d;
    --slate-dark: #232526;
    --slate-light: #55585a;
  }
  * { box-sizing: border-box; margin: 0; padding: 0; }
  html, body { width: 1200px; height: 1023px; overflow: hidden; }
  body {
    background: var(--page);
    font-family: "Open Sans", Arial, sans-serif;
    position: relative;
  }
  .card {
    position: absolute;
    left: 250px;
    width: 700px;
    height: 400px;
    border-radius: 18px;
    overflow: hidden;
    box-shadow: 0 10px 26px rgba(0,0,0,0.22);
  }
  /* front */
  .card-front {
    top: 70px;
    background: linear-gradient(180deg, var(--card-white) 0%, var(--card-mist) 100%);
  }
  .brand {
    position: absolute;
    left: 48px;
    top: 52px;
    display: flex;
    align-items: center;
    gap: 16px;
  }
  .brand-square {
    width: 62px;
    height: 62px;
    border-radius: 6px;
    background: var(--slate);
  }
  .brand-name {
    font-family: "Cinzel", Georgia, serif;
    font-weight: 400;
    font-size: 68px;
    letter-spacing: 2px;
    color: var(--ink);
    line-height: 1;
  }
  .person {
    position: absolute;
    left: 50px;
    top: 160px;
  }
  .person-name {
    font-family: "Cinzel", Georgia, serif;
    font-weight: 400;
    font-size: 28px;
    color: var(--orange);
    letter-spacing: 1px;
  }
  .person-role {
    font-size: 15px;
    color: var(--ink-soft);
    margin-top: 2px;
  }
  .contact {
    position: absolute;
    left: 50px;
    top: 246px;
    list-style: none;
    font-size: 16px;
    color: var(--ink-soft);
  }
  .contact li {
    display: flex;
    align-items: center;
    gap: 9px;
    height: 26px;
  }
  .contact svg { width: 15px; height: 15px; flex: none; }
  .office {
    position: absolute;
    left: 440px;
    top: 168px;
    font-size: 16px;
    line-height: 1.45;
    color: var(--ink);
  }
  .office-name {
    color: var(--orange);
    font-weight: 600;
  }
  .footer-band {
    position: absolute;
    left: 0; right: 0; bottom: 0;
    height: 72px;
    background: linear-gradient(90deg, #8d8f90 0%, var(--slate-light) 40%, var(--slate-dark) 100%);
  }
  .web-tab {
    position: absolute;
    left: 470px;
    right: 0;
    bottom: 72px;
    height: 40px;
    background: linear-gradient(180deg, var(--orange) 0%, var(--orange-deep) 100%);
    display: flex;
    align-items: center;
    padding-left: 34px;
    font-size: 17px;
    letter-spacing: 1px;
    color: var(--slate-dark);
  }
  /* back */
  .card-back {
    top: 540px;
    background: linear-gradient(135deg, var(--slate-light) 0%, var(--slate) 45%, var(--slate-dark) 100%);
  }
  .card-back svg.back-stripes {
    position: absolute;
    inset: 0;
    width: 100%;
    height: 100%;
  }
  .back-name {
    position: absolute;
    left: 0; right: 0;
    top: 140px;
    text-align: center;
    font-family: "Cinzel", Georgia, serif;
    font-weight: 400;
    font-size: 110px;
    letter-spacing: 10px;
    color: rgba(20,21,22,0.45);
  }
</style>
</head>
<body>
  <section class="card card-front" aria-label="Business card front">
    <div class="brand">
      <span class="brand-square"></span>
      <span class="brand-name">TBRITE</span>
    </div>
    <div class="person">
      <p class="person-name">Linda Marchbank</p>
      <p class="person-role">Director</p>
    </div>
    <ul class="contact">
      <li>
        <svg viewBox="0 0 16 16" aria-hidden="true"><circle cx="8" cy="8" r="8" fill="#e0521f"/><path d="M5.2 4.2l1.6-.2.8 1.9-1 .8a5 5 0 0 0 2.7 2.7l.8-1 1.9.8-.2 1.6c-3.6.3-6.9-3-6.6-6.6z" fill="#fff"/></svg>
        07853 416207
      </li>
      <li>
        <svg viewBox="0 0 16 16" aria-hidden="true"><circle cx="8" cy="8" r="8" fill="#e0521f"/><rect x="4" y="5.2" width="8" height="5.6" rx=".6" fill="#fff"/><path d="M4.3 5.6L8 8.4l3.7-2.8" stroke="#e0521f" stroke-width=".9" fill="none"/></svg>
        lmarchbank@tbrite.co.uk
      </li>
    </ul>
    <address class="office" style="font-style:normal">
      <span class="office-name">Tbrite</span><br>
      Maple Court, Elmstead Lane<br>
      Brackley, NN13 4QT
    </address>
    <div class="web-tab">www.tbrite.co.uk</div>
    <div class="footer-band"></div>
  </section>

  <section class="card card-back" aria-label="Business card back">
    <svg class="back-stripes" viewBox="0 0 700 400" preserveAspectRatio="none" aria-hidden="true">
      <polygon points="0,40 0,140 260,400 360,400" fill="rgba(255,255,255,0.06)"/>
      <polygon points="0,150 0,210 190,400 250,400" fill="rgba(0,0,0,0.12)"/>
    </svg>
    <p class="back-name">TBRITE</p>
  </section>
</body>
</html>
```